Postcard Design www.harborlineclaims.example

We need a new postcard design that would show our over 25 years of knowledge and expertise, yet touch on the functions and services we can perform, in Medical Billing. The problem is that the competition is fierce, with many many new Medical Billing Companies getting in the act. Unfortunately these companies can be extremely hurtful to the financial well being of medical providers, as they do not know the laws, regulations, nor have the expertise.
Updates

I just received my final approval on my trademark, so the phrase Where Patience Pays & Detail Delivers is now a registered trademark. Also I just realized on my original postcard there is a typo. It should read Over 25 years in claims, billing, and revenue recovery, the "the" should not be there. Also I would like the "free 10 chart/EOB audit" to be a bigger deal that would catch the readers eye, maybe an expiration date or some other "call to action"

Target Market(s)

Target business is medical professionals. Chiropractors, Home Health providers, providers that would have large insurance clientele (Vitalcover, PPO).
NOT targeting Familiy Practice, Pediatricians, Hospitals, Dentists.

Industry/Entity Type

Financial

Font styles to use
Serif
Sans Serif

Colors
ec1f27
3277b5
ffffff

Requirements
Must have
• New ideas not just copied from my existing postcard. Something that somehow tells the story of going with inexperience can cost you.

```html
<!DOCTYPE html>
<html lang="en">
<head>
<meta charset="utf-8">
<title>Harborline Claims &amp; Audit – Postcard</title>
<link href="https://fonts.googleapis.com/css2?family=PT+Sans+Narrow:wght@400;700&family=PT+Sans:wght@400;700&family=Tinos:wght@400&family=Arimo:wght@400&display=swap" rel="stylesheet">
<style>
  :root{
    --red:#ec1f27;
    --red-deep:#d8222b;
    --blue:#3277b5;
    --blue-band:#2164ad;
    --blue-deep:#1d5c9a;
    --blue-soft:#8eb1d9;
    --navy:#183f80;
    --ink:#2a2a2a;
    --white:#ffffff;
    --stage:#e9e4dc;
    --rule:#b9b9b9;
  }
  *{box-sizing:border-box;margin:0;padding:0}
  html,body{width:1200px;height:500px;overflow:hidden}
  body{background:var(--stage);position:relative;font-family:"PT Sans",sans-serif}
  .card{position:absolute;top:33px;height:432px;background:var(--white);overflow:hidden;box-shadow:0 2px 6px rgba(0,0,0,.18)}
  .front{left:22px;width:560px}
  .back{left:615px;width:563px}

  /* front */
  .brand{position:absolute;left:20px;top:30px;display:flex;align-items:center;gap:12px}
  .brand-dot{width:40px;height:40px;border-radius:50%;background:var(--red-deep);flex:none}
  .brand-name{font-family:"Tinos",serif;font-size:26px;line-height:29px;color:var(--ink)}
  .tagline{position:absolute;left:142px;top:97px;font-family:"Tinos",serif;font-size:14.5px;color:var(--ink)}
  .money-photo{position:absolute;right:0;top:0;width:160px;height:116px;background:linear-gradient(135deg,#c7d0b6,#8e9f7c 60%,#d8cfa4)}
  .headline{position:absolute;left:0;width:100%;top:116px;text-align:center;font-family:"PT Sans",sans-serif;font-weight:700;font-size:25px;line-height:34px;color:var(--red-deep)}
  .benefits{position:absolute;left:0;top:150px;width:100%;height:73px;background:var(--blue-band);padding:5px 0 0 30px;list-style:none}
  .benefits li{position:relative;color:var(--white);font-family:"PT Sans",sans-serif;font-weight:700;font-size:14.5px;line-height:21px;padding-left:12px}
  .benefits li svg{position:absolute;left:-4px;top:5px}
  .offer{position:absolute;left:0;top:223px;width:100%;height:114px;background:var(--blue-soft)}
  .seal{position:absolute;left:14px;top:29px;width:56px;height:56px;border-radius:50%;background:radial-gradient(circle,#e8c768,#b68a2a)}
  .experience{position:absolute;left:74px;top:16px;width:138px;text-align:center;font-family:"PT Sans",sans-serif;font-weight:700}
  .experience strong{display:block;font-size:16px;line-height:18px;color:#1d4f9c}
  .experience span{display:block;font-size:11px;line-height:13px;color:#1a1a1a;margin-top:4px}
  .coupon{position:absolute;left:222px;top:7px;width:328px;height:100px;background:var(--white);border:2px dashed var(--red-deep);text-align:center;font-family:"PT Sans",sans-serif;font-weight:700}
  .coupon-tag{position:absolute;left:-2px;top:-2px;background:var(--red-deep);color:var(--white);font-size:10px;letter-spacing:1px;line-height:15px;padding:0 6px}
  .coupon-title{margin-top:10px;font-size:22px;line-height:25px;color:var(--blue-deep)}
  .coupon-value{font-size:14px;line-height:18px;color:#1a1a1a}
  .coupon-deadline{position:absolute;left:0;right:0;bottom:0;background:var(--red-deep);color:var(--white);font-size:13.5px;line-height:24px}
  .contact-band{position:absolute;left:0;top:337px;width:100%;height:55px;background:var(--red-deep);text-align:center;color:var(--white);font-family:"PT Sans Narrow",sans-serif}
  .contact-band .addr{font-size:15px;line-height:18px;padding-top:5px}
  .contact-band .phones{font-weight:700;font-size:19px;line-height:24px}
  .website{position:absolute;left:0;width:100%;top:392px;text-align:center;font-family:"PT Sans",sans-serif;font-weight:700;font-size:18px;line-height:38px;letter-spacing:2.5px;color:#1a1a1a}

  /* back */
  .paid-photo{position:absolute;left:0;top:0;width:157px;height:154px;background:linear-gradient(145deg,#7a4a22,#c8924f 50%,#e2c08a)}
  .rookie{position:absolute;left:157px;top:0;width:116px;height:154px;background:var(--blue-soft);color:var(--white);text-align:center;font-family:"PT Sans",sans-serif;font-weight:700;font-size:20px;line-height:25px;padding-top:14px}
  .recover{position:absolute;left:0;top:154px;width:273px;height:80px;background:var(--blue-deep);color:var(--white);text-align:center;font-family:"PT Sans",sans-serif;font-weight:700;font-size:19px;line-height:24px;padding-top:16px}
  .help{position:absolute;left:0;top:234px;width:273px;height:58px;text-align:center;font-family:"PT Sans",sans-serif;font-weight:700;font-size:22px;letter-spacing:1.5px;line-height:58px;color:#1a1a1a}
  .call{position:absolute;left:0;top:292px;width:273px;height:65px;background:var(--red-deep);color:var(--white);text-align:center;font-family:"PT Sans Narrow",sans-serif;font-weight:700;font-size:19px;line-height:22px;padding-top:10px}
  .call svg{vertical-align:-2px;margin:0 2px}
  .mail-brand{position:absolute;left:296px;top:24px;display:flex;align-items:center;gap:6px}
  .mail-brand .brand-dot{width:22px;height:22px}
  .mail-brand .brand-name{font-size:12px;line-height:13px}
  .mail-brand small{display:block;font-size:7px;line-height:9px}
  .return-addr{position:absolute;left:278px;top:64px;width:160px;text-align:center;font-family:"Arimo",sans-serif;font-size:10.5px;line-height:12.5px;color:#1a1a1a}
  .stamp{position:absolute;left:495px;top:22px;width:55px;height:50px;border:1px solid var(--rule)}
  .address-line{position:absolute;left:295px;width:238px;height:1px;background:var(--rule)}
</style>
</head>
<body>

<section class="card front">
  <div class="brand">
    <span class="brand-dot"></span>
    <span class="brand-name">HARBORLINE CLAIMS<br>&amp; AUDIT</span>
  </div>
  <p class="tagline">Where Patience Pays &amp; Detail Delivers&reg;</p>
  <div class="money-photo" role="img" aria-label="Photo of dollar bills with a gold key"></div>

  <h1 class="headline">How much money is hiding in your charts?</h1>

  <ul class="benefits">
    <li><svg width="11" height="11" viewBox="0 0 10 10"><polygon points="5,0 6.2,3.6 10,3.7 7,6 8.1,9.8 5,7.5 1.9,9.8 3,6 0,3.7 3.8,3.6" fill="#ec1f27"/></svg>New billers learn the rules on your money – I already know them</li>
    <li><svg width="11" height="11" viewBox="0 0 10 10"><polygon points="5,0 6.2,3.6 10,3.7 7,6 8.1,9.8 5,7.5 1.9,9.8 3,6 0,3.7 3.8,3.6" fill="#ec1f27"/></svg>Guaranteed methods to increase your collectibles</li>
    <li><svg width="11" height="11" viewBox="0 0 10 10"><polygon points="5,0 6.2,3.6 10,3.7 7,6 8.1,9.8 5,7.5 1.9,9.8 3,6 0,3.7 3.8,3.6" fill="#ec1f27"/></svg>Let me turn your denied/delayed claims into CASH in your POCKETS</li>
  </ul>

  <div class="offer">
    <div class="seal" role="img" aria-label="Gold 25 years seal"></div>
    <div class="experience">
      <strong>Over 25 Years of Experience</strong>
      <span>in claims, billing, and revenue recovery – PPO, HMO, Vitalcover</span>
    </div>
    <div class="coupon">
      <span class="coupon-tag">LIMITED OFFER</span>
      <p class="coupon-title">FREE 10-Chart/EOB Audit</p>
      <p class="coupon-value">A $500.00–$1,200.00 VALUE – yours at no cost</p>
      <p class="coupon-deadline">Offer expires June 30 · Call today to claim it!</p>
    </div>
  </div>

  <div class="contact-band">
    <p class="addr">4580 Tidewater Blvd, Suite 210, Port Alder, CA 90000</p>
    <p class="phones">Toll Free (844) 555-0147 Fax (844) 555-0148</p>
  </div>
  <p class="website">www.harborlineclaims.example</p>
</section>

<section class="card back">
  <div class="paid-photo" role="img" aria-label="Photo of paid claim envelopes"></div>
  <h2 class="rookie">DON'T<br>LET A<br>ROOKIE<br>COST<br>YOU</h2>
  <p class="recover">Recover Your Lost/<br>Hidden Profits Today!</p>
  <p class="help">LET US HELP</p>
  <p class="call">Call <svg width="15" height="15" viewBox="0 0 16 16"><circle cx="8" cy="8" r="7" fill="none" stroke="#fff" stroke-width="1.5"/><path d="M5.5 4.5c.6-.4 1-.2 1.3.4l.5 1c.2.4 0 .7-.3 1-.3.2-.3.5-.1.9.4.7.9 1.2 1.6 1.6.4.2.7.2.9-.1.3-.3.6-.5 1-.3l1 .5c.6.3.8.7.4 1.3-.7 1-2 1.1-3.4.1C6.9 9.9 6 9 5.1 7.8 4.2 6.4 4.5 5.2 5.5 4.5z" fill="#fff"/></svg> by June 30 – Free Audit<br>(844) 555-0147</p>

  <div class="mail-brand">
    <span class="brand-dot"></span>
    <span class="brand-name">HARBORLINE CLAIMS<br>&amp; AUDIT<small>Where Patience Pays &amp; Detail Delivers&reg;</small></span>
  </div>
  <p class="return-addr">4580 Tidewater Blvd,<br>Suite 210, Port Alder, CA 90000</p>
  <div class="stamp"></div>
  <div class="address-line" style="top:197px"></div>
  <div class="address-line" style="top:235px"></div>
  <div class="address-line" style="top:272px"></div>
  <div class="address-line" style="top:305px"></div>
</section>

</body>
</html>
```